Real Estate Business Card

On the front side I want to have my info, my brokerage info.
On the back side I want have my complany’s logo, website and Facebook link. I will provide all this once I select a design.

I would like to see Black background and gold text, Dark Blue and gold text and White and blue text designs

Font styles to use
Sans Serif
Script

```html
<!DOCTYPE html>
<html lang="en">
<head>
<meta charset="utf-8">
<title>Harbor Key Homes – Business Card</title>
<link rel="stylesheet" href="https://fonts.googleapis.com/css2?family=Cinzel:wght@600&family=Open+Sans:wght@400;600&display=swap">
<style>
  :root {
    --stage: #2b2b2d;
    --navy: #12305a;
    --navy-deep: #0e2748;
    --gold: #f2c12e;
    --gold-dark: #c8961a;
    --white: #ffffff;
    --rule: rgba(242, 193, 46, 0.35);
  }
  * { box-sizing: border-box; margin: 0; padding: 0; }
  html, body { width: 1200px; height: 896px; overflow: hidden; }
  body {
    background: var(--stage);
    font-family: "Open Sans", Arial, sans-serif;
    display: flex;
    flex-direction: column;
    align-items: center;
    justify-content: center;
    gap: 48px;
  }
  .card {
    position: relative;
    width: 700px;
    height: 400px;
    background: var(--navy);
    border-bottom: 14px solid var(--gold);
    box-shadow: 0 16px 30px rgba(0,0,0,0.45);
    color: var(--white);
    overflow: hidden;
  }
  .card::after {
    content: "";
    position: absolute;
    left: 0; right: 0; bottom: 0;
    height: 4px;
    background: var(--gold-dark);
  }
  .brand-name {
    font-family: "Cinzel", Georgia, serif;
    font-weight: 600;
    color: var(--gold);
    letter-spacing: 2px;
    line-height: 1.05;
    text-align: center;
  }
  .brand-mark { display: flex; align-items: center; gap: 14px; }
  .brand-dot { width: 16px; height: 16px; background: var(--gold); border-radius: 50%; }

  /* front */
  .card--front .agent { position: absolute; left: 44px; top: 44px; }
  .agent-name {
    font-family: "Cinzel", Georgia, serif;
    font-weight: 600;
    color: var(--gold);
    font-size: 30px;
    letter-spacing: 1px;
  }
  .agent-title { font-size: 19px; margin-bottom: 12px; }
  .contact-list { list-style: none; font-size: 18px; line-height: 1.45; }
  .contact-list li { display: flex; align-items: center; gap: 10px; }
  .contact-list svg { width: 16px; height: 16px; fill: var(--gold); flex: none; }
  .card--front .brand-mark { position: absolute; right: 48px; top: 150px; }
  .card--front .brand-name { font-size: 40px; }
  .card--front .office {
    position: absolute; right: 48px; bottom: 46px; text-align: right;
    font-size: 19px; line-height: 1.35;
  }
  .office-web { color: var(--gold); font-weight: 600; border-bottom: 1px solid var(--rule); padding-bottom: 4px; margin-bottom: 6px; }

  /* back */
  .card--back { display: flex; flex-direction: column; align-items: center; justify-content: center; gap: 26px; }
  .card--back .brand-name { font-size: 50px; }
  .social-link { font-size: 20px; }
</style>
</head>
<body>

<section class="card card--front" aria-label="Card front">
  <div class="agent">
    <h1 class="agent-name">Dorian Vale</h1>
    <p class="agent-title">Managing Director</p>
    <ul class="contact-list">
      <li><svg viewBox="0 0 16 16"><path d="M3 1h3l1.5 4-2 1.3a9 9 0 0 0 4.2 4.2L11 8.5l4 1.5v3a2 2 0 0 1-2 2A13 13 0 0 1 1 3a2 2 0 0 1 2-2z"/></svg>055-987 654 321</li>
      <li><svg viewBox="0 0 16 16"><path d="M4 0h8a1 1 0 0 1 1 1v14a1 1 0 0 1-1 1H4a1 1 0 0 1-1-1V1a1 1 0 0 1 1-1zm1 2v10h6V2z"/></svg>055-987 654 321</li>
      <li><svg viewBox="0 0 16 16"><path d="M0 3h16v10H0zm1.5 1.2V5l6.5 4 6.5-4v-.8L8 8z"/></svg>hello@harborkeyhomes.com</li>
      <li><svg viewBox="0 0 16 16"><circle cx="8" cy="8" r="7"/></svg>www.harborkeyhomes.com</li>
    </ul>
  </div>
  <div class="brand-mark">
    <span class="brand-dot"></span>
    <p class="brand-name">Harbor Key<br>Homes</p>
  </div>
  <div class="office">
    <p class="office-web">www.harborkeyhomes.com</p>
    <p>48 Linden Row, Eastport Bayland</p>
    <p>Postal 204815</p>
  </div>
</section>

<section class="card card--back" aria-label="Card back">
  <div class="brand-mark">
    <span class="brand-dot"></span>
    <p class="brand-name">Harbor Key Homes</p>
  </div>
  <p class="social-link">www.socialpage.com/harborkeyhomes</p>
</section>

</body>
</html>
```